Design a styled business card for an intimacy and attachment psychologist

I am a Psychologist providing online therapy to patients across the United States. My work is interpersonal and emotion-focused, with an emphasis on the client-therapist relationship. My primary areas of work are very personal, including sexuality and gender, abuse and trauma, and grief and loss. My target audience will be adults of all ages 18+.
My business card should convey a warm and inviting feeling of professionalism that is also casual and comfortable.
The front should be fairly simple and professional, consisting of:
- My name, Dr. Rosalind Petrakis
- My title, Licensed Psycholigist
- My logo
On either the front or the back, my contact information should be listed:
- ros@drrospetrakis.example
- 555.014.7788
- drrospetrakis.example
On the rear, I would like a description of the areas that I specialize in. This can be formatted in any way that appears stylistically interesting.
Individual and Couples
Relationships and Infidelity
Sexual Health & Aging
Gender Identity & Sexual Orientation
Abuse and Trauma
Sexual Compulsivity & Addiction
Sexual Dysfunction
Target Market(s)
My target audience will be adults of all ages 18+.
Industry/Entity Type
Psychology
Contact Information for Business Card
The front should be fairly simple and professional, consisting of: - My name, Dr. Rosalind Petrakis - My title, Licensed Psycholigist - My logo On either the front or the back, my contact information should be listed: - ros@drrospetrakis.example - 555.014.7788 - drrospetrakis.example On the rear, I would like a description of the areas that I specialize in. This can be formatted in any way that appears stylistically interesting. Individual and Couples Relationships and Infidelity Sexual Health & Aging Gender Identity & Sexual Orientation Abuse and Trauma Sexual Compulsivity & Addiction Sexual Dysfunction
- Follow brand guide

```html
<!DOCTYPE html>
<html lang="en">
<head>
<meta charset="utf-8">
<title>Dr. Rosalind Petrakis — Business Card</title>
<link href="https://fonts.googleapis.com/css2?family=Montserrat:wght@400;500;600;700&display=swap" rel="stylesheet">
<style>
  :root {
    --stage: #2b2b2d;
    --card: #ffffff;
    --card-soft: #f4f4f4;
    --ink: #1d1d1f;
    --navy: #2a2350;
    --orange: #f09c1c;
    --red: #e23a35;
    --emboss: #e6e6e6;
    --emboss-line: #dcdcdc;
  }
  * { box-sizing: border-box; margin: 0; padding: 0; }
  html, body { width: 1200px; height: 780px; overflow: hidden; }
  body {
    background: var(--stage);
    font-family: "Montserrat", Arial, sans-serif;
    color: var(--ink);
    position: relative;
  }
  .card {
    position: absolute;
    top: 240px;
    width: 525px;
    height: 300px;
    background: var(--card);
    overflow: hidden;
    box-shadow: 0 10px 30px rgba(0,0,0,.45);
  }
  .card--front { left: 50px; background: var(--card-soft); }
  .card--back { left: 625px; }

  .card__art { position: absolute; inset: 0; width: 100%; height: 100%; }

  .wordmark {
    position: absolute;
    display: flex;
    align-items: center;
    gap: 10px;
    font-weight: 600;
    color: var(--navy);
    font-size: 17px;
    line-height: 1.15;
    letter-spacing: .04em;
    text-transform: uppercase;
  }
  .wordmark__dot {
    width: 44px; height: 44px; border-radius: 50%;
    background: var(--navy);
    flex: none;
  }
  .card--front .wordmark { left: 34px; top: 26px; }
  .card--back .wordmark { left: 36px; top: 82px; font-size: 19px; }
  .card--back .wordmark__dot { width: 52px; height: 52px; }

  .contact {
    position: absolute;
    left: 40px; top: 104px;
    list-style: none;
    font-size: 12.5px;
    font-weight: 500;
    line-height: 1.7;
  }
  .contact li { display: flex; align-items: center; gap: 8px; }
  .contact svg { width: 12px; height: 12px; flex: none; }

  .identity {
    position: absolute;
    right: 40px; top: 112px;
    text-align: right;
  }
  .identity__name { font-size: 21px; font-weight: 700; color: var(--orange); }
  .identity__title { font-size: 15px; font-weight: 500; margin-top: 4px; }

  .divider {
    position: absolute;
    left: 270px; top: 40px;
    width: 1px; height: 220px;
    background: var(--ink);
  }
  .specialties {
    position: absolute;
    left: 292px; top: 44px;
  }
  .specialties__heading {
    font-size: 15px; font-weight: 700;
    color: var(--orange);
    letter-spacing: .03em;
    margin-bottom: 6px;
  }
  .specialties__list { list-style: none; font-size: 11.5px; font-weight: 500; line-height: 1.72; }
  .specialties__list li { display: flex; align-items: center; gap: 6px; }
  .specialties__list li::before {
    content: ""; width: 8px; height: 8px; border-radius: 50%;
    background: var(--navy); flex: none;
  }
</style>
</head>
<body>

<section class="card card--front" aria-label="Card front">
  <svg class="card__art" viewBox="0 0 525 300" preserveAspectRatio="none" aria-hidden="true">
    <circle cx="395" cy="215" r="92" fill="none" stroke="var(--emboss-line)" stroke-width="3"/>
    <path d="M0 135 C40 190 120 230 220 245 C280 255 330 265 350 300 L0 300 Z" fill="var(--orange)"/>
    <path d="M12 128 C48 190 130 226 218 238" fill="none" stroke="var(--red)" stroke-width="5"/>
    <path d="M350 300 C340 285 333 278 325 272 L345 262 C352 270 360 285 366 300 Z" fill="var(--red)"/>
    <rect x="497" y="215" width="28" height="50" fill="var(--red)"/>
  </svg>

  <div class="wordmark"><span class="wordmark__dot"></span><span>Dr. Rosalind<br>Petrakis</span></div>

  <ul class="contact">
    <li><svg viewBox="0 0 12 12"><path d="M3 1 L5 3.5 L4 5 C5 7 6 8 7.5 8.5 L9 7.5 L11 9.5 L9.5 11 C5 11 1 7 1 2.5 Z" fill="var(--orange)"/></svg>555.014.7788</li>
    <li><svg viewBox="0 0 12 12"><rect x="1" y="2.5" width="10" height="7" rx="1" fill="var(--orange)"/><path d="M1.5 3 L6 6.5 L10.5 3" fill="none" stroke="#fff" stroke-width="1"/></svg>ros@drrospetrakis.example</li>
    <li><svg viewBox="0 0 12 12"><circle cx="6" cy="6" r="5" fill="var(--orange)"/><path d="M1 6 H11 M6 1 C3.5 4 3.5 8 6 11 M6 1 C8.5 4 8.5 8 6 11" fill="none" stroke="#fff" stroke-width=".8"/></svg>www.drrospetrakis.example</li>
  </ul>

  <div class="identity">
    <p class="identity__name">Dr. Rosalind Petrakis</p>
    <p class="identity__title">Licensed Psycholigist</p>
  </div>
</section>

<section class="card card--back" aria-label="Card back">
  <svg class="card__art" viewBox="0 0 525 300" preserveAspectRatio="none" aria-hidden="true">
    <circle cx="400" cy="140" r="118" fill="none" stroke="var(--emboss)" stroke-width="3"/>
  </svg>

  <div class="wordmark"><span class="wordmark__dot"></span><span>Dr. Rosalind<br>Petrakis</span></div>

  <div class="divider"></div>

  <div class="specialties">
    <h2 class="specialties__heading">SPECIALIZE</h2>
    <ul class="specialties__list">
      <li>Abuse and Trauma</li>
      <li>Sexual Dysfunction</li>
      <li>Sexual Health &amp; Aging</li>
      <li>Stylistically interesting</li>
      <li>Individual and Couples</li>
      <li>Relationships and Infidelity</li>
      <li>Sexual Compulsivity &amp; Addiction</li>
      <li>Gender Identity &amp; Sexual Orientation</li>
    </ul>
  </div>
</section>

</body>
</html>
```